Business Card Design

I am a cosmetic tattooist in Melbourne Australia, who provides services where by I tattoo eyebrows in block or strokes with a tattooing gun. Feathering that mimic hair strands with a scalpel. Eyeliner top and bottom with the tattooing gun. Lips just as either an outline or a full block colour where the top and bottom lip is completely covered. Corrections for tattooing done previously that have either faded to quickly, turned blue or orange due to bad colour choice, or a mishap. Paramedical colouring for people who either have scaring that needs to be matched to their skin colour. Patients who have alopecia or a skin condition that needs hair like tattooing. Cancer patients who's nipples and areolas have been partially or totally been removed and require them to be re drawn into the new skin. I colour match with a variety of inks (around 50) at my disposal and can also lift colours with a pigmentation lifter. I also require the use of two different types of anaesthetics throughout each procedure.
Colours that I have looked into the represent health, professionalism, beauty, skin and medical type procedures are Light to dark brown, Light to dark grey, Black and White. Possibly a splash of red to represent the lips. I am mobile and can work from any venue that takes a commission for a bed. I have completed a diploma in cosmetic tattooing being qualified.
Updates

Project Deadline Extended
Reason: I have been awaiting for a design from own more designer who accepted my project but hasn't released their design.

Project Deadline Extended

Industry/Entity Type

Medical

Contact Information for Business Card

Company name: Velora Cosmetic Tattooing
Name: Joanne Pilbury
Title: Cosmetic and Paramedical Tattooist
Address: P.O Box 2863, Ashcombe Rise, Victoria 3187
Mobile: 0417385926
Email: veloracosmetictattooing@examplemail.net
Preferred colours: Light brown, Light Grey, Black (writing) White Background

Requirements
Nice to have
• A shape of the eyebrow or eye with eyeliner in the background. Possibly red lips. No straight lines, only curved or curled lines.

```html
<!DOCTYPE html>
<html lang="en">
<head>
<meta charset="utf-8">
<title>Velora Cosmetic Tattooing – Business Cards</title>
<link rel="stylesheet" href="https://fonts.googleapis.com/css2?family=Open+Sans:wght@400;600&display=swap">
<style>
  :root {
    --backdrop: #e8e6e3;
    --card: #ffffff;
    --brand-red: #a3282b;
    --ink: #111111;
    --ink-soft: #2b2b2b;
    --eye-light: #f4f5f6;
    --eye-mid: #b9bcc0;
    --eye-dark: #3a3b3e;
  }
  * { box-sizing: border-box; margin: 0; padding: 0; }
  html, body {
    width: 1200px; height: 1200px; overflow: hidden;
    background: var(--backdrop);
    font-family: "Open Sans", Arial, sans-serif;
  }
  .sheet { position: relative; width: 1200px; height: 1200px; }
  .card {
    position: absolute; left: 146px;
    width: 907px; height: 559px;
    background: var(--card);
    overflow: hidden;
    box-shadow: 0 2px 6px rgba(0,0,0,0.12);
  }
  .card--first { top: 32px; }
  .card--second { top: 612px; }

  .eye-visual {
    position: absolute; left: 496px; top: 0;
    width: 411px; height: 432px;
    background:
      radial-gradient(ellipse 60% 45% at 62% 48%, var(--eye-dark) 0%, var(--eye-mid) 45%, rgba(255,255,255,0) 80%),
      radial-gradient(ellipse 70% 40% at 75% 22%, var(--eye-mid) 0%, var(--eye-light) 60%, rgba(255,255,255,0) 100%);
  }

  .brand-name {
    position: absolute; left: 36px; top: 70px;
    color: var(--brand-red);
    font-weight: 400;
    font-size: 46px; line-height: 1.2;
  }
  .brand-name span { display: block; }
  .brand-name .brand-name__second { padding-left: 130px; }

  .holder { position: absolute; left: 46px; top: 328px; }
  .holder__name {
    font-size: 29px; font-weight: 600; color: var(--ink);
    line-height: 1.2;
  }
  .holder__title {
    font-size: 20px; color: var(--ink-soft); margin-top: 6px;
  }
  .contact-list { list-style: none; margin-top: 20px; }
  .contact-list li {
    display: flex; align-items: center; gap: 16px;
    font-size: 19px; color: var(--ink); height: 39px;
  }
  .contact-icon { width: 24px; height: 24px; flex: none; }
</style>
</head>
<body>
<main class="sheet">

  <section class="card card--first">
    <div class="eye-visual" role="img" aria-label="Close-up photograph of an eye with long lashes and glittering silver eyeshadow"></div>
    <h1 class="brand-name"><span>Velora Cosmetic</span><span class="brand-name__second">Tattooing</span></h1>
    <div class="holder">
      <p class="holder__name">Joanne Pilbury</p>
      <p class="holder__title">Cosmetic and Paramedical Tattooist</p>
      <ul class="contact-list">
        <li><svg class="contact-icon" viewBox="0 0 24 24"><circle cx="12" cy="12" r="12" fill="#111"/><path d="M12 5a4.5 4.5 0 0 0-4.5 4.5c0 3.4 4.5 8.5 4.5 8.5s4.5-5.1 4.5-8.5A4.5 4.5 0 0 0 12 5zm0 6.3a1.8 1.8 0 1 1 0-3.6 1.8 1.8 0 0 1 0 3.6z" fill="#fff"/></svg>P.O Box 2863, Ashcombe Rise, Victoria 3187</li>
        <li><svg class="contact-icon" viewBox="0 0 24 24"><circle cx="12" cy="12" r="12" fill="#111"/><path d="M8.4 6l2 2.6-1.2 1.4c.8 1.8 2.1 3.1 3.9 3.9l1.4-1.2 2.6 2-1.3 2.1c-4.6-.4-8.3-4.1-8.7-8.7z" fill="#fff"/></svg>0417385926</li>
        <li><svg class="contact-icon" viewBox="0 0 24 24"><circle cx="12" cy="12" r="12" fill="#111"/><rect x="6" y="8" width="12" height="8.5" rx="1" fill="#fff"/><path d="M6.5 8.7L12 13l5.5-4.3" stroke="#111" stroke-width="1.2" fill="none"/></svg>veloracosmetictattooing@examplemail.net</li>
      </ul>
    </div>
  </section>

  <section class="card card--second">
    <div class="eye-visual" role="img" aria-label="Close-up photograph of an eye with long lashes and glittering silver eyeshadow"></div>
    <h1 class="brand-name"><span>Velora Cosmetic</span><span class="brand-name__second">Tattooing</span></h1>
    <div class="holder">
      <p class="holder__name">Joanne Pilbury</p>
      <p class="holder__title">Cosmetic and Paramedical Tattooist</p>
      <ul class="contact-list">
        <li><svg class="contact-icon" viewBox="0 0 24 24"><circle cx="12" cy="12" r="12" fill="#111"/><path d="M12 5a4.5 4.5 0 0 0-4.5 4.5c0 3.4 4.5 8.5 4.5 8.5s4.5-5.1 4.5-8.5A4.5 4.5 0 0 0 12 5zm0 6.3a1.8 1.8 0 1 1 0-3.6 1.8 1.8 0 0 1 0 3.6z" fill="#fff"/></svg>P.O Box 2863, Ashcombe Rise, Victoria 3187</li>
        <li><svg class="contact-icon" viewBox="0 0 24 24"><circle cx="12" cy="12" r="12" fill="#111"/><path d="M8.4 6l2 2.6-1.2 1.4c.8 1.8 2.1 3.1 3.9 3.9l1.4-1.2 2.6 2-1.3 2.1c-4.6-.4-8.3-4.1-8.7-8.7z" fill="#fff"/></svg>0417385926</li>
        <li><svg class="contact-icon" viewBox="0 0 24 24"><circle cx="12" cy="12" r="12" fill="#111"/><rect x="6" y="8" width="12" height="8.5" rx="1" fill="#fff"/><path d="M6.5 8.7L12 13l5.5-4.3" stroke="#111" stroke-width="1.2" fill="none"/></svg>veloracosmetictattooing@examplemail.net</li>
      </ul>
    </div>
  </section>

</main>
</body>
</html>
```